Design a website for selling rare gemstones and expensive jewelry

I have URL www.kelvadro.com and need to redo the website. The site I want to build will offer rare expensive gemstones called Kelvadro. Some of these gemstones cost millions of dollars!
I like the websites below for the example of quality I am looking for:
Www.carrowmotors.com
Www.vance-hollismotorcars.com
Www.Dravo.com
Www.orsette.com
And Henri Castel website.
It must be simple but elegant and very high end.
Also need SEO work and all marketing done for the site.
I like the sun and beach with the palm trees and beautiful model look along with the high end Carrow/ Vance-Hollis feel….
Zumvo “Beautiful Brazilian Beach”…..

```html
<!DOCTYPE html>
<html lang="en">
<head>
<meta charset="utf-8">
<title>Kelvadro — Everlasting Jewellery</title>
<link rel="stylesheet" href="https://fonts.googleapis.com/css2?family=Bodoni+Moda:ital,opsz,wght@0,6..96,400;1,6..96,400&family=Jost:wght@400;500&display=swap">
<style>
  :root {
    --paper: #ffffff;
    --ink: #141414;
    --muted: #6e6e6e;
    --rule: #e6e4e0;
    --photo-light: #efedea;
    --photo-mid: #6f6b68;
    --photo-dark: #1c1b1d;
    --serif: "Bodoni Moda", "Didot", serif;
    --sans: "Jost", "Helvetica Neue", sans-serif;
  }
  * { margin: 0; padding: 0; box-sizing: border-box; }
  html, body {
    width: 1200px; height: 683px; overflow: hidden;
    background: var(--paper); color: var(--ink);
    font-family: var(--sans);
  }
  .site { position: relative; width: 1200px; height: 683px; }

  .site-header {
    position: absolute; left: 0; top: 0; width: 1200px; height: 127px;
    border-bottom: 1px solid var(--rule);
  }
  .search {
    position: absolute; left: 86px; top: 31px;
    display: flex; align-items: center; gap: 16px;
    font-size: 12px; color: var(--muted);
  }
  .brand {
    position: absolute; left: 0; right: 0; top: 26px; text-align: center;
    font-family: var(--serif); font-size: 34px; letter-spacing: 2px;
    color: var(--ink);
  }
  .header-tools {
    position: absolute; left: 960px; top: 30px; display: flex; gap: 22px;
  }
  .main-nav {
    position: absolute; left: 0; right: 0; top: 94px;
    display: flex; justify-content: center; gap: 56px;
    font-size: 15px; font-weight: 400;
  }
  .main-nav a { color: var(--ink); text-decoration: none; }

  .hero-copy { position: absolute; left: 118px; top: 262px; }
  .hero-eyebrow {
    position: absolute; left: 0; top: 18px;
    font-size: 10px; letter-spacing: 0.5px; text-transform: uppercase;
  }
  .hero-title {
    font-family: var(--serif); font-weight: 400; font-size: 46px;
    line-height: 55px; letter-spacing: -0.5px; text-transform: uppercase;
  }
  .hero-title .indent { padding-left: 82px; }
  .hero-title em { text-transform: none; font-style: italic; }
  .shop-now {
    position: absolute; left: 292px; top: 228px;
    display: flex; align-items: center; gap: 12px;
    font-family: var(--serif); font-style: italic; font-size: 14px;
    color: var(--ink); text-decoration: none;
  }

  .hero-photo {
    position: absolute; left: 600px; top: 127px; width: 600px; height: 435px;
    background: linear-gradient(160deg, var(--photo-light) 0%, var(--photo-mid) 55%, var(--photo-dark) 100%);
  }
</style>
</head>
<body>
<div class="site">
  <header class="site-header">
    <div class="search">
      <svg width="22" height="22" viewBox="0 0 22 22" fill="none" stroke="#141414" stroke-width="1.6"><circle cx="9.5" cy="9.5" r="7"/><line x1="14.6" y1="14.6" x2="20" y2="20"/></svg>
      <span>Search</span>
    </div>
    <div class="brand">KELVADRO</div>
    <div class="header-tools">
      <svg width="24" height="22" viewBox="0 0 24 22" fill="none" stroke="#141414" stroke-width="1.6" aria-label="Wishlist"><path d="M12 20 L3.5 11.5 A5 5 0 0 1 12 4.5 A5 5 0 0 1 20.5 11.5 Z" stroke-linejoin="round"/></svg>
      <svg width="22" height="24" viewBox="0 0 22 24" fill="none" stroke="#141414" stroke-width="1.6" aria-label="Bag"><path d="M3 7 H19 L18 22 H4 Z" stroke-linejoin="round"/><path d="M7.5 9 V5.5 A3.5 3.5 0 0 1 14.5 5.5 V9"/></svg>
    </div>
    <nav class="main-nav">
      <a href="#">Home</a><a href="#">Shop</a><a href="#">About</a><a href="#">Contact</a>
    </nav>
  </header>

  <section class="hero-copy">
    <span class="hero-eyebrow">Discover</span>
    <h1 class="hero-title">
      <span class="indent">Everlasting</span><br>
      Jewellery<br>
      The <em>world’s</em> Best<br>
      Makers &amp;<br>
      Dealers
    </h1>
    <a class="shop-now" href="#">Shop Now
      <svg width="22" height="12" viewBox="0 0 22 12" fill="none" stroke="#141414" stroke-width="1.6"><line x1="1" y1="6" x2="20" y2="6"/><path d="M15 1.5 L20 6 L15 10.5"/></svg>
    </a>
  </section>

  <div class="hero-photo" role="img" aria-label="Photo of a model in a wide black hat and black top wearing a gold chain with a turquoise gemstone pendant"></div>
</div>
</body>
</html>
```